New Modern floristry business design

Hi, we are a new business based in Sydney called "velvet moss floristry"

With so many floristry's we need a good design that will set a great first impression.

A few descriptive words on how we envision velvet moss floristry:

-dynamic design
-minimal colour (colour can be used to enhance the design)
-black white grey (can include gold,silver,metallic shadowing)
Strong "VELVET MOSS" with a classy "FLORISTRY"
Bold with a touch of feminine

Industry/Entity Type

Business

Contact Information for Business Card

Velvet Moss Floristry,
Delphine Ruvek,
Velvetmossfloristry@quillmail.com.au

```html
<!DOCTYPE html>
<html lang="en">
<head>
<meta charset="utf-8">
<title>Velvet Moss Floristry – Business Card</title>
<link rel="stylesheet" href="https://fonts.googleapis.com/css2?family=Poiret+One&display=swap">
<style>
  :root {
    --canvas-bg: #2a2a2a;
    --card-bg: #151515;
    --card-bg-light: #1f1f1f;
    --accent: #d6db1c;
    --accent-dim: rgba(214, 219, 28, 0.55);
    --sheen: rgba(255, 255, 255, 0.05);
    --bloom-pink: #e58aa8;
    --bloom-red: #c8313c;
    --bloom-green: #5d6b4e;
    --bloom-rose: #b98a8e;
  }
  * { box-sizing: border-box; margin: 0; padding: 0; }
  html, body {
    width: 1200px;
    height: 900px;
    overflow: hidden;
    background: var(--canvas-bg);
  }
  .canvas {
    position: relative;
    width: 1200px;
    height: 900px;
    font-family: "Poiret One", "Century Gothic", sans-serif;
    color: var(--accent);
  }
  .card {
    position: absolute;
    left: 250px;
    width: 700px;
    height: 389px;
    background: radial-gradient(ellipse at 40% 40%, var(--card-bg-light), var(--card-bg) 70%);
    border: 1.5px solid var(--accent-dim);
    overflow: hidden;
  }
  .card--front { top: 40px; }
  .card--back { top: 471px; }
  .card__sheen {
    position: absolute;
    inset: 0;
    width: 100%;
    height: 100%;
  }
  .card__sheen path {
    fill: none;
    stroke: var(--sheen);
    stroke-width: 1.5;
  }
  .wordmark {
    position: absolute;
    white-space: nowrap;
    font-weight: 400;
    color: var(--accent);
    letter-spacing: 0.02em;
  }
  .card--front .wordmark {
    left: 190px;
    top: 200px;
    font-size: 52px;
    line-height: 1;
  }
  .card--front .wordmark__sub {
    display: block;
    margin-left: 150px;
    margin-top: 6px;
    font-size: 40px;
  }
  .card--back .wordmark {
    left: 60px;
    top: 70px;
    font-size: 46px;
  }
  .bouquet {
    position: absolute;
    left: 205px;
    top: 55px;
    width: 240px;
    height: 120px;
    border-radius: 50% 50% 45% 45%;
    background: radial-gradient(ellipse at 50% 45%, var(--bloom-pink), var(--bloom-red) 60%, transparent 72%);
  }
  .wreath {
    position: absolute;
    left: 30px;
    bottom: 0;
    width: 240px;
    height: 160px;
    opacity: 0.6;
    background: radial-gradient(ellipse at 50% 55%, transparent 22%, var(--bloom-rose) 32%, var(--bloom-green) 58%, transparent 72%);
  }
  .contact {
    position: absolute;
    right: 60px;
    text-align: left;
    white-space: nowrap;
  }
  .contact__name {
    top: 165px;
    right: 70px;
    font-size: 40px;
  }
  .contact__email {
    top: 250px;
    right: 40px;
    font-size: 24px;
  }
</style>
</head>
<body>
<main class="canvas">

  <section class="card card--front" aria-label="Card front">
    <svg class="card__sheen" viewBox="0 0 700 389" aria-hidden="true">
      <path d="M-20 320 C 200 180, 420 120, 720 160"/>
      <path d="M-20 360 C 240 220, 460 180, 720 230"/>
      <path d="M260 -10 C 320 120, 300 260, 380 400"/>
    </svg>
    <div class="bouquet" role="img" aria-label="Bunch of pink and red gerbera flowers"></div>
    <h1 class="wordmark">VELVET MOSS <span class="wordmark__sub">FLORISTRY</span></h1>
  </section>

  <section class="card card--back" aria-label="Card back">
    <svg class="card__sheen" viewBox="0 0 700 389" aria-hidden="true">
      <path d="M-20 300 C 180 200, 420 140, 720 190"/>
      <path d="M-20 350 C 230 240, 470 200, 720 260"/>
      <path d="M330 -10 C 380 120, 360 260, 440 400"/>
    </svg>
    <h2 class="wordmark">VELVET MOSS FLORISTRY</h2>
    <p class="contact contact__name">Delphine Ruvek</p>
    <p class="contact contact__email">velvetmossfloristry@quillmail.com.au</p>
    <div class="wreath" role="img" aria-label="Heart-shaped wreath of roses and cabbage leaves"></div>
  </section>

</main>
</body>
</html>
```